New Flyer Design Project - for sale units at The Lodge phase 3

on attached the A2 is full kitchen 1 bedroom, the A3 is gally kitchen and the B2 is the the 2 bedroom, on attached pictures the room with 2 queen beds is only for the 2 bedroom

This is going to be used to sale the units (real estate sale) so the layout could possibly be text and then pictures maybe 1 bedroom on one side and 2 on the back?

Experience the Modern Luxury of the New Phase 3 Building of the
Lodge at Harlow Bend

* Opening Spring 2019

* America's #17 Family Resort; Tennessee's Only Ranked Resort

1 Bedroom Bunk Suite (Galley Kitchen) - $199,000; Sleeps 6

* Private King Master Bedroom

* Bunk Bed Galley

* Granite Counters Throughout

* Fully Furnished with Custom Furnishings

* Private Balcony

* Equipped Galley Kitchen

* In Unit Laundry

* Queen Sleeper Sofa

1 Bedroom Bunk Suite (Full Kitchen) - $209,000; Sleeps 6

* Bunk Bed Galley

* Granite Counters throughout

* Equipped Full Kitchen

* Completely Furnished with Custom Furnishings

* Private Balcony

* In Unit Laundry

* Queen Sleeper Sofa

2 Bedroom Bunk Suite (Full Kitchen) - $249,000; Sleeps 10

* Private King Master Bedroom with On-Suite Bathroom

* Two Queen Bedroom

* Bunk Bed Galley

* Full Kitchen

* Private Balcony

* In Unit Laundry

* Queen Sleeper Sofa

Target Market(s)

people wanting to buy units in phase 3 of The Lodge at Harlow Bend

Industry/Entity Type

Real Estate Development

Requirements
Must have
• attached text to describe units and price
• pictures and layouts
• Contact Dale Porter
• 865-730-2958 Dale@brightfernretreats.example
Nice to have
• brand and logo
Should not have
• it should not be plain this is m ore of a luxury project

```html
<!DOCTYPE html>
<html lang="en">
<head>
<meta charset="utf-8">
<title>The Lodge at Harlow Bend – Phase 3 Sales Flyer</title>
<link href="https://fonts.googleapis.com/css2?family=Oswald:wght@400;500;600&family=Roboto+Slab:wght@300;400;500&display=swap" rel="stylesheet">
<style>
:root{
  --brown:#5b4433;
  --brown-dark:#4a3628;
  --copper:#c27c3c;
  --copper-light:#e6a768;
  --orange:#f0a052;
  --gray:#dcdddb;
  --page:#ffffff;
  --bg:#cfcfcd;
  --ink:#5b4433;
}
*{margin:0;padding:0;box-sizing:border-box}
html,body{width:1200px;height:830px;overflow:hidden;background:var(--bg)}
.sheet{position:absolute;top:58px;width:510px;height:720px;background:var(--page);overflow:hidden;box-shadow:0 8px 22px rgba(0,0,0,.25)}
.front{left:80px}
.back{left:622px}
.abs{position:absolute}
.photo{position:absolute}
.copper-grad{background:linear-gradient(90deg,var(--copper) 0%,var(--copper-light) 55%,var(--copper) 100%)}

/* front */
.front .brand{left:22px;top:112px;width:180px;text-align:center;font-family:'Roboto Slab',serif;font-weight:500;font-size:21px;line-height:1.15;color:var(--brown)}
.ranking{left:0;top:286px;width:486px;height:43px;background:var(--brown);color:#fff;font-family:'Oswald',sans-serif;font-weight:500;font-size:17px;line-height:43px;padding-left:20px;letter-spacing:-.2px}
.ranking .num{color:var(--orange);font-size:26px}
.headline{left:26px;top:340px;color:#fff}
.headline .lead{font-family:'Oswald',sans-serif;font-weight:500;font-size:28px;line-height:1.1}
.headline .l2{font-family:'Roboto Slab',serif;font-size:18px;line-height:1.3;margin-top:6px}
.headline .l3{font-family:'Roboto Slab',serif;font-size:17px;line-height:1.2}
.headline .l3 i{font-weight:300}
.headline .l4{font-family:'Roboto Slab',serif;font-weight:300;font-style:italic;font-size:13px}
.opening{right:28px;top:364px;text-align:right}
.opening .year{font-family:'Oswald',sans-serif;font-weight:600;font-size:40px;line-height:1;color:var(--brown)}
.opening .season{font-family:'Oswald',sans-serif;font-size:15px;letter-spacing:1px;color:var(--orange)}
.unit-title{font-family:'Oswald',sans-serif;font-size:13px;color:var(--orange);line-height:1.35}
.unit-price{font-family:'Oswald',sans-serif;font-weight:600;color:var(--brown);line-height:1.1}
.front .unit{right:24px;top:489px;text-align:right}
.front .unit-price{font-size:27px;margin-top:8px}
.features{list-style:none;font-family:'Roboto Slab',serif;font-size:8.5px;line-height:1.25}
.features li{position:relative;padding-left:16px;margin-bottom:6px}
.features li::before{content:"";position:absolute;left:0;top:2px;width:9px;height:6px;background:var(--copper);clip-path:polygon(0 40%,50% 0,100% 40%,85% 100%,15% 100%)}
.front .features{color:var(--ink)}
.about-tab{left:302px;top:613px;width:208px;height:67px;color:#fff;text-align:center;padding-left:38px;padding-top:10px;font-family:'Roboto Slab',serif;font-size:19px;line-height:1.15;clip-path:polygon(22% 0,100% 0,100% 100%,0 100%)}
.about-tab b{font-weight:500}

/* back */
.back .unit-a{left:37px;top:40px;color:#fff}
.back .unit-a .t{font-family:'Oswald',sans-serif;font-size:12.5px;line-height:1.4}
.back .unit-a .p{font-family:'Oswald',sans-serif;font-weight:500;font-size:25px;line-height:1.1;color:var(--orange);margin-top:5px;white-space:nowrap}
.back .rule{left:37px;top:100px;width:47px;height:2px;background:var(--orange)}
.back .features.dark{color:#fff}
.back .unit-b{right:37px;top:327px;text-align:right}
.back .unit-b .unit-price{font-size:30px;margin-top:10px}
.back .unit-b .note{font-family:'Roboto Slab',serif;font-size:8px;color:var(--ink);margin-top:8px}
.about-head{left:24px;top:575px;color:#fff;font-family:'Roboto Slab',serif;font-size:12.5px}
.about-head b{font-weight:500}
.call{left:280px;top:580px;width:230px;height:68px;background:var(--brown);clip-path:polygon(8% 0,100% 0,100% 100%,0 100%);text-align:center;padding-left:20px;padding-top:8px}
.call .k{font-family:'Roboto Slab',serif;font-size:17px;color:var(--orange);line-height:1.1}
.call .n{font-family:'Oswald',sans-serif;font-weight:500;font-size:27px;color:#fff;line-height:1.2}
.contact-bar{left:0;top:680px;width:510px;height:30px;background:var(--brown);color:#fff;display:flex;align-items:center;justify-content:center;gap:10px;font-family:'Roboto Slab',serif;font-size:8.5px}
.contact-bar .name{font-family:'Oswald',sans-serif;font-weight:500;font-size:16px}
.contact-bar .sep{opacity:.8}
</style>
</head>
<body>

<section class="sheet front">
  <svg class="abs" width="510" height="720" style="left:0;top:0">
    <defs>
      <linearGradient id="cu" x1="0" x2="1">
        <stop offset="0" stop-color="#b9733a"/><stop offset=".55" stop-color="#e6a768"/><stop offset="1" stop-color="#c27c3c"/>
      </linearGradient>
      <linearGradient id="room" x1="0" y1="0" x2="1" y2="1">
        <stop offset="0" stop-color="#d9dcc8"/><stop offset=".5" stop-color="#c8bda4"/><stop offset="1" stop-color="#6f7a74"/>
      </linearGradient>
    </defs>
    <polygon points="26,21 486,21 486,264 26,264" fill="url(#room)"/>
    <polygon points="26,21 40,21 200,264 26,264" fill="#dcdddb"/>
    <polygon points="38,0 50,0 230,288 206,288" fill="url(#cu)"/>
    <rect x="0" y="264" width="250" height="24" fill="url(#cu)"/>
    <polygon points="0,329 272,329 344,463 0,463" fill="url(#cu)"/>
    <polygon points="284,329 510,329 510,463 356,463" fill="#dcdddb"/>
    <polygon points="0,680 296,680 270,720 0,720" fill="#dcdddb"/>
  </svg>
  <div class="photo" role="img" aria-label="Rendering of the suite dining area and kitchen" style="left:200px;top:21px;width:286px;height:243px;background:linear-gradient(135deg,#d7dbbf,#b8ab8e 55%,#5e6b66)"></div>
  <div class="abs brand">The Lodge<br>at Harlow Bend</div>
  <div class="abs ranking">AMERICA'S <span class="num">#17</span> FAMILY RESORT; TENNESSEE'S ONLY RANKED RESORT</div>
  <div class="abs headline">
    <div class="lead">Experience</div>
    <div class="l2">THE MODERN LUXURY</div>
    <div class="l3"><i>of the</i> New Phase 3 Building</div>
    <div class="l4">of the Lodge at Harlow Bend</div>
  </div>
  <div class="abs opening"><div class="year">2019</div><div class="season">OPENING SPRING</div></div>
  <div class="photo" role="img" aria-label="Rendering of the king master bedroom" style="left:24px;top:469px;width:158px;height:125px;background:linear-gradient(135deg,#c9d1a3,#ecebe3 50%,#6d7b78)"></div>
  <div class="photo" role="img" aria-label="Rendering of the bathroom vanity" style="left:188px;top:469px;width:158px;height:125px;background:linear-gradient(135deg,#d2d6c0,#e7e3d9 45%,#4a3a30)"></div>
  <div class="abs unit">
    <div class="unit-title">1 BEDROOM BUNK SUITE<br>(GALLEY KITCHEN)</div>
    <div class="unit-price">$199,000;<br>SLEEPS 6</div>
  </div>
  <ul class="abs features" style="left:27px;top:608px;width:150px">
    <li>Private King Master Bedroom</li>
    <li>Bunk Bed Galley</li>
    <li>Granite Counters Throughout</li>
    <li>Fully Furnished with Custom Furnishings</li>
  </ul>
  <ul class="abs features" style="left:178px;top:608px;width:130px">
    <li>Private Balcony</li>
    <li>Equipped Galley Kitchen</li>
    <li>In Unit Laundry</li>
    <li>Queen Sleeper Sofa</li>
  </ul>
  <div class="abs about-tab copper-grad">ABOUT<br><b>PROPERTY</b></div>
</section>

<section class="sheet back">
  <svg class="abs" width="510" height="720" style="left:0;top:0">
    <defs>
      <linearGradient id="cu2" x1="0" x2="1">
        <stop offset="0" stop-color="#b9733a"/><stop offset=".55" stop-color="#e6a768"/><stop offset="1" stop-color="#c27c3c"/>
      </linearGradient>
      <linearGradient id="cu3" x1="0" y1="0" x2="0" y2="1">
        <stop offset="0" stop-color="#5b4433"/><stop offset=".45" stop-color="#5b4433"/><stop offset=".65" stop-color="#c27c3c"/><stop offset="1" stop-color="#e3a364"/>
      </linearGradient>
    </defs>
    <rect x="0" y="0" width="510" height="13" fill="#f0a052"/>
    <polygon points="0,13 445,13 428,46 306,46 232,261 0,261" fill="#5b4433"/>
    <polygon points="258,270 276,270 195,434 178,434" fill="url(#cu2)"/>
    <polygon points="0,445 290,445 242,678 0,678" fill="url(#cu3)"/>
    <rect x="0" y="710" width="510" height="10" fill="#f0a052"/>
  </svg>
  <div class="photo" role="img" aria-label="Rendering of the two queen bedroom" style="left:238px;top:61px;width:272px;height:239px;clip-path:polygon(29.4% 0,100% 0,100% 100%,2.2% 100%);background:linear-gradient(135deg,#cdd4a6,#efeee6 50%,#6a7774)"></div>
  <div class="photo" role="img" aria-label="Rendering of the full kitchen and dining area" style="left:0;top:270px;width:258px;height:164px;clip-path:polygon(0 0,100% 0,76% 100%,0 100%);background:linear-gradient(135deg,#d2d7bd,#e9e4d6 50%,#5c6865)"></div>
  <div class="photo" role="img" aria-label="Rendering of the bathroom" style="left:34px;top:467px;width:152px;height:83px;clip-path:polygon(20% 0,100% 0,80% 100%,0 100%);background:linear-gradient(135deg,#e5e2d8,#b7ad99 50%,#3f3129)"></div>
  <div class="photo" role="img" aria-label="Rendering of the dining room" style="left:178px;top:467px;width:152px;height:83px;clip-path:polygon(20% 0,100% 0,80% 100%,0 100%);background:linear-gradient(135deg,#d8dcc6,#c8bda2 50%,#4e4a45)"></div>
  <div class="photo" role="img" aria-label="Rendering of the master bedroom" style="left:322px;top:467px;width:152px;height:83px;clip-path:polygon(20% 0,100% 0,80% 100%,0 100%);background:linear-gradient(135deg,#ccd3a5,#eeede5 50%,#6e7b78)"></div>

  <div class="abs unit-a">
    <div class="t">1 BEDROOM BUNK SUIT (FULL KITCHEN)</div>
    <div class="p">$209,000; SLEEPS 6</div>
  </div>
  <div class="abs rule"></div>
  <ul class="abs features dark" style="left:37px;top:114px;width:200px;font-size:8px">
    <li style="margin-bottom:5.5px">Private King Master Bedroom</li>
    <li style="margin-bottom:5.5px">Bunk Bed Galley</li>
    <li style="margin-bottom:5.5px">Granite Counters throughout</li>
    <li style="margin-bottom:5.5px">Equipped Full Kitchen</li>
    <li style="margin-bottom:5.5px">Completely Furnished with Custom Furnishings</li>
    <li style="margin-bottom:5.5px">Private Balcony</li>
    <li style="margin-bottom:5.5px">In Unit Laundry</li>
    <li style="margin-bottom:5.5px">Queen Sleeper Sofa</li>
  </ul>

  <div class="abs unit-b">
    <div class="unit-title">2 BEDROOM BUNK SUITE<br>(FULL KITCHEN)</div>
    <div class="unit-price">$249,000;<br>SLEEPS 10</div>
    <div class="note">Private King Master Bedroom with On-Suite Bathroom</div>
  </div>

  <div class="abs about-head">ABOUT <b>PROPERTY</b></div>
  <ul class="abs features dark" style="left:25px;top:603px;width:110px;font-size:8px">
    <li style="margin-bottom:5px">Two Queen Bedroom</li>
    <li style="margin-bottom:5px">Bunk Bed Galley</li>
    <li style="margin-bottom:5px">Granite Counters Throughout</li>
    <li style="margin-bottom:5px">Full Kitchen</li>
  </ul>
  <ul class="abs features dark" style="left:142px;top:603px;width:110px;font-size:8px">
    <li style="margin-bottom:5px">Completely Furnished with Custom Furnishings</li>
    <li style="margin-bottom:5px">Private Balcony</li>
    <li style="margin-bottom:5px">In Unit Laundry</li>
    <li style="margin-bottom:5px">Queen Sleeper Sofa</li>
  </ul>

  <div class="abs call"><div class="k">CALL NOW</div><div class="n">865-730-2958</div></div>

  <div class="abs contact-bar">
    <span>Dale@brightfernretreats.example</span><span class="sep">|</span>
    <span class="name">DALE PORTER</span><span class="sep">|</span>
    <span>418 Alder Creek Road, Pine Hollow, Tennessee 37999</span>
  </div>
</section>

</body>
</html>
```